Business card design needed

Bright Path Ahead is an online wellness program designed for people dealing with cancer to take control of their lives and bright path ahead.

Target Market(s)

initially woman aged 35 to 65 years eventaully then men

Industry/Entity Type

Business

Contact Information for Business Card

Marlena Throsby
Bright path ahead Coach
Marlena@brightpathway.com.au
M 0418392716
Skype Marlena.Throsby
local number to come
www.brightpathway.com.au

Requirements
Must have
• Business cards want to have a photo of me on the back this is a head shot. Also a small blurb " Marlena recovered and survived 2 types of cancer. She under went a transformational 12 month journey to overcome cancer naturally . Join her online coaching program to bright path ahead.

Phone number and email and skype address.
Nice to have
• Looking for something that resembles health EG abstract tree of life, or something resembling health and balance . Like lime green/apple green want modern fresh. Want only 2 colours used on the cards. Need to use the logo and Bright path ahead on website and email signature - Clean and fresh

Also would like Letter head and logo for website and email signature

```html
<!DOCTYPE html>
<html lang="en">
<head>
<meta charset="utf-8">
<title>Bright Path Ahead – Business Card</title>
<link rel="stylesheet" href="https://fonts.googleapis.com/css2?family=Questrial&display=swap">
<style>
  :root {
    --page-bg: #e9eaec;
    --card-light: #f7f7f8;
    --card-mid: #e4e5e7;
    --ink: #2b2b2d;
    --ink-soft: #555558;
    --brand-dark: #1b3a9c;
    --brand-mid: #1f5fbf;
    --brand-light: #2fa8de;
    --white: #ffffff;
  }
  * { box-sizing: border-box; margin: 0; padding: 0; }
  html, body {
    width: 1200px;
    height: 900px;
    overflow: hidden;
    background: var(--page-bg);
    font-family: "Questrial", "Century Gothic", sans-serif;
    color: var(--ink);
  }
  .sheet {
    width: 1200px;
    height: 900px;
    display: flex;
    align-items: center;
    justify-content: center;
    gap: 40px;
  }
  .card {
    position: relative;
    width: 560px;
    height: 320px;
    overflow: hidden;
    background: linear-gradient(135deg, var(--card-light) 0%, var(--card-mid) 100%);
    box-shadow: 0 6px 18px rgba(0, 0, 0, 0.18);
  }

  /* Front face */
  .brand-name {
    position: absolute;
    left: 36px;
    top: 92px;
    width: 230px;
    font-size: 44px;
    line-height: 1.05;
    color: var(--brand-mid);
    letter-spacing: -0.5px;
  }
  .contact-block {
    position: absolute;
    left: 290px;
    top: 100px;
  }
  .contact-name {
    font-size: 20px;
    color: var(--ink);
  }
  .contact-role {
    font-size: 13px;
    color: var(--ink);
    margin-bottom: 14px;
  }
  .contact-list { list-style: none; }
  .contact-list li {
    display: flex;
    align-items: center;
    gap: 7px;
    font-size: 15px;
    line-height: 22px;
    color: var(--ink);
  }
  .contact-icon {
    width: 14px;
    height: 14px;
    flex: none;
  }

  /* Back face */
  .portrait {
    position: absolute;
    right: 0;
    top: 0;
    width: 270px;
    height: 250px;
    background: radial-gradient(ellipse at 55% 40%, #e2c7ae 0%, #cfb79c 30%, #e9e6e1 70%, #f1f1f2 100%);
  }
  .blurb {
    position: absolute;
    left: 30px;
    top: 42px;
    width: 258px;
    text-align: right;
    font-size: 13px;
    line-height: 16px;
    color: var(--ink-soft);
  }
  .blurb p + p { margin-top: 14px; }
  .url-band {
    position: absolute;
    left: 0;
    right: 0;
    top: 252px;
    height: 38px;
    background: linear-gradient(90deg, var(--brand-dark) 0%, var(--brand-mid) 70%, var(--brand-light) 100%);
    display: flex;
    align-items: center;
    justify-content: center;
    color: var(--white);
    font-size: 24px;
    letter-spacing: 0.2px;
  }
</style>
</head>
<body>
<main class="sheet">

  <section class="card card-front" aria-label="Card front">
    <div class="brand-name">Bright Path Ahead</div>
    <div class="contact-block">
      <div class="contact-name">Marlena Throsby</div>
      <div class="contact-role">Bright path ahead Coach</div>
      <ul class="contact-list">
        <li>
          <svg class="contact-icon" viewBox="0 0 14 14" aria-hidden="true">
            <rect x="0.5" y="2.5" width="13" height="9" rx="1" fill="var(--brand-mid)"/>
            <path d="M1 3 L7 8 L13 3" fill="none" stroke="#fff" stroke-width="1.2"/>
          </svg>
          Marlena@brightpathway.com.au
        </li>
        <li>
          <svg class="contact-icon" viewBox="0 0 14 14" aria-hidden="true">
            <rect x="3.5" y="0.5" width="7" height="13" rx="1.5" fill="var(--brand-mid)"/>
            <rect x="4.7" y="2" width="4.6" height="8" fill="#fff"/>
          </svg>
          0418392716
        </li>
        <li>
          <svg class="contact-icon" viewBox="0 0 14 14" aria-hidden="true">
            <circle cx="7" cy="7" r="6.5" fill="var(--brand-mid)"/>
          </svg>
          4570218863
        </li>
        <li>
          <svg class="contact-icon" viewBox="0 0 14 14" aria-hidden="true">
            <circle cx="7" cy="7" r="6.5" fill="var(--brand-light)"/>
          </svg>
          Marlena.Throsby
        </li>
      </ul>
    </div>
  </section>

  <section class="card card-back" aria-label="Card back">
    <div class="portrait" role="img" aria-label="Head-and-shoulders portrait photo of the coach, smiling, chin resting on her hand"></div>
    <div class="blurb">
      <p>Marlena recovered and<br>survived 2 types of cancer.</p>
      <p>She under went<br>a transformational 12 month journey<br>to overcome cancer naturally.</p>
      <p>Join her online coaching program<br>to bright path ahead.</p>
    </div>
    <div class="url-band">www.brightpathway.com.au</div>
  </section>

</main>
</body>
</html>
```